Business card Zottelgarten

Business card is for a self-employed dog trainer with own dog school. Name and logo of the dog school are available. Color specifications as well. The design should be classy and minimalist, but also modern. An already existing idea would be: Front: Only the logo Back: Contact data

Font styles to use
Serif
Sans Serif
Other font styles liked:
• Trajan Pro

Colors
f78f20

Requirements
Must have
• Name: Margit Wendler-Rasch Title: Dipl. Dog Trainer Contain my logo Follow my font and color preferences (see files)

```html
<!DOCTYPE html>
<html lang="de">
<head>
<meta charset="utf-8">
<title>Zottelgarten – Visitenkarte</title>
<link href="https://fonts.googleapis.com/css2?family=Cinzel:wght@400;600&family=Lato:wght@400;700&display=swap" rel="stylesheet">
<style>
  :root {
    --brown: #7a6656;
    --tan: #c9b39c;
    --white: #ffffff;
    --ink: #2a2522;
    --stage: #e9e4de;
  }
  * { margin: 0; padding: 0; box-sizing: border-box; }
  html, body { width: 1200px; height: 901px; overflow: hidden; }
  body {
    background: var(--stage);
    font-family: "Lato", sans-serif;
    position: relative;
  }
  .card {
    position: absolute;
    left: 320px;
    width: 560px;
    height: 320px;
    overflow: hidden;
    box-shadow: 0 6px 18px rgba(0,0,0,0.18);
  }
  /* Front */
  .card--front { top: 100px; background: var(--brown); }
  .front-mark {
    position: absolute;
    left: 50%;
    top: 42px;
    transform: translateX(-50%);
    width: 124px;
    height: 124px;
    border-radius: 50%;
    border: 3px solid var(--white);
  }
  .front-name {
    position: absolute;
    top: 186px;
    width: 100%;
    text-align: center;
    font-family: "Cinzel", serif;
    font-weight: 400;
    font-size: 42px;
    letter-spacing: 2px;
    color: var(--white);
  }
  .front-url {
    position: absolute;
    top: 242px;
    width: 100%;
    text-align: center;
    font-family: "Cinzel", serif;
    font-size: 11px;
    letter-spacing: 7px;
    color: var(--white);
  }
  /* Back */
  .card--back { top: 480px; background: var(--white); }
  .back-wave { position: absolute; inset: 0; width: 100%; height: 100%; }
  .back-logo { position: absolute; left: 34px; top: 26px; width: 240px; text-align: center; }
  .back-mark {
    width: 74px; height: 74px; border-radius: 50%;
    background: var(--brown);
    margin: 0 auto 6px;
  }
  .back-name {
    font-family: "Cinzel", serif;
    font-size: 26px;
    letter-spacing: 1px;
    color: var(--brown);
  }
  .back-url {
    font-family: "Cinzel", serif;
    font-size: 7px;
    letter-spacing: 4px;
    color: var(--brown);
    margin-top: 2px;
  }
  .contact-list {
    position: absolute;
    left: 40px;
    top: 150px;
    list-style: none;
    font-size: 14px;
    color: var(--ink);
    line-height: 21px;
  }
  .contact-list li { display: flex; align-items: center; gap: 10px; }
  .contact-list svg { width: 12px; height: 12px; fill: var(--ink); flex: none; }
  .person {
    position: absolute;
    right: 34px;
    top: 110px;
    text-align: right;
  }
  .person-name { font-weight: 700; font-size: 22px; color: var(--brown); }
  .person-title { font-size: 14px; color: var(--ink); margin-top: 2px; }
  .address {
    position: absolute;
    right: 34px;
    top: 210px;
    text-align: right;
    font-size: 16px;
    line-height: 21px;
    color: var(--ink);
  }
</style>
</head>
<body>

<section class="card card--front" aria-label="Kartenvorderseite">
  <div class="front-mark"></div>
  <div class="front-name">ZOTTELGARTEN</div>
  <div class="front-url">WWW.ZOTTELGARTEN.CH</div>
</section>

<section class="card card--back" aria-label="Kartenrückseite">
  <svg class="back-wave" viewBox="0 0 560 320" preserveAspectRatio="none" aria-hidden="true">
    <path d="M0 220 C120 250 200 290 300 320 L0 320 Z" fill="var(--tan)"/>
    <path d="M40 240 C160 270 260 300 330 305 C420 310 500 295 560 280 L560 320 L0 320 L0 250 Z" fill="var(--brown)"/>
  </svg>

  <div class="back-logo">
    <div class="back-mark"></div>
    <div class="back-name">ZOTTELGARTEN</div>
    <div class="back-url">WWW.ZOTTELGARTEN.CH</div>
  </div>

  <ul class="contact-list">
    <li><svg viewBox="0 0 12 12"><path d="M2.5 0.5l2 2-1 1.5c.7 1.5 2 2.8 3.5 3.5l1.5-1 2 2-1.2 2C5 10.5 1.5 7 0.5 1.7z"/></svg>079 555 01 20</li>
    <li><svg viewBox="0 0 12 12"><path d="M3 0h6v12H3zM4 1.5v7.5h4V1.5z"/></svg>079 555 01 78</li>
    <li><svg viewBox="0 0 12 12"><path d="M0 2h12v8H0zM1 3l5 3.5L11 3z" fill-rule="evenodd"/></svg>info@zottelgarten.com</li>
    <li><svg viewBox="0 0 12 12"><circle cx="6" cy="6" r="5.5"/></svg>www.zottelgarten.com</li>
  </ul>

  <div class="person">
    <div class="person-name">Margit Wendler-Rasch</div>
    <div class="person-title">Dipl. Hundetrainerin</div>
  </div>

  <div class="address">
    Lindenweg 14<br>
    CH-8400 Winterthur
  </div>
</section>

</body>
</html>
```